Help our pizza bases / flat breads fly off the shelves - You'll be seen in supermarkets New Zealand

Packaging design.
We have bought a product that is in desperate need of a complete re-brand. This includes a name, and a package design.
It is an rectangle shaped flat bread that can be used in many ways, and is presented 5 in a pack, in an unprinted flexible formed bottom, with a flat top film applied that is flat and ready to receive your design.
The product is mainly used as a pizza base bought by Mums to feed the family. It is also can be a pre dinner nibble like a pizza bread, and for quick and easy, you can cut one into 3 pieces, and toast in a pop-up toaster, before topping with whatever is in your fridge.
The current name is "Kelmo breads" which is just silly. The brand "Kelmo" needs to change to "Dugald's Flat Breads" or whatever you might suggest. The product name might be "Tavira Pizza Base" or "Tavira Flat bread" as you like.
The look must get consumers to pick up the product and have a closer look. The nature of the graphics should emphasize the versatility and multi-usefulness, so the consumer can imagine what they will do with the product when they get it home. I feel that an informative pack will be better than a beautiful pack to get more sales. I have uploaded pictures showing the product currently in Supermarkets, and also a picture of the current product. Dimensions are 310 x 130mm.
You will need to leave room for: Barcode, Nutritional Panel, Cooking instructions, Storage instructions, Ingredients list and Company contact details - each one say 45 x 45mm or similar.
These details could go on the bottom of the low long side, as this is obscured while on shelf (see photo)
You will also highlight in your design, Preservative Free, 100% Natural, 5 Bases, Made with Olive oil, Hand made, and the variant (Roasted Garlic, or Original)
You will want to highlight the uses like: Pizza base, pizza bread, cut toast and top or similar.

```html
<!DOCTYPE html>
<html lang="en">
<head>
<meta charset="utf-8">
<title>Marlo Bakery – Tavira Pizza Bases</title>
<link href="https://fonts.googleapis.com/css2?family=Oswald:wght@400;500;700&family=Roboto+Slab:wght@700&family=Lato:wght@400;700&display=swap" rel="stylesheet">
<style>
  :root {
    --page: #ffffff;
    --wood-light: #f6dc8a;
    --wood-mid: #ecc869;
    --wood-dark: #e2b65a;
    --ink: #3b1d12;
    --teal: #1aa2b7;
    --teal-deep: #128ea2;
    --red: #b5161c;
    --red-deep: #9a1015;
    --cream: #fff7e6;
  }
  * { box-sizing: border-box; }
  html, body {
    margin: 0;
    width: 1200px;
    height: 1000px;
    overflow: hidden;
    background: var(--page);
  }
  .canvas {
    position: relative;
    width: 1200px;
    height: 1000px;
  }
  .pack {
    position: absolute;
    left: 150px;
    width: 900px;
    height: 378px;
    --band: var(--teal);
    --band-deep: var(--teal-deep);
  }
  .pack--original { top: 70px; }
  .pack--garlic { top: 545px; --band: var(--red); --band-deep: var(--red-deep); }

  .pack__tab {
    position: absolute;
    left: 270px;
    top: -34px;
    width: 190px;
    height: 70px;
    border-radius: 60px 60px 0 0;
    background: var(--wood-light);
  }
  .pack__label {
    position: absolute;
    inset: 0;
    overflow: hidden;
    background: linear-gradient(172deg, var(--wood-light) 0%, var(--wood-mid) 45%, var(--wood-dark) 100%);
  }
  .brand {
    position: absolute;
    left: 250px;
    top: 4px;
    display: flex;
    align-items: center;
    gap: 10px;
    font-family: "Oswald", sans-serif;
    font-weight: 500;
    font-size: 34px;
    color: var(--ink);
  }
  .brand__dot {
    width: 16px;
    height: 16px;
    border-radius: 50%;
    background: var(--ink);
  }
  .product-line {
    position: absolute;
    left: 290px;
    top: 52px;
    font-family: "Oswald", sans-serif;
    font-weight: 500;
    font-size: 40px;
    line-height: 1;
    color: var(--ink);
  }
  .product-name {
    position: absolute;
    left: 210px;
    top: 94px;
    font-family: "Oswald", sans-serif;
    font-weight: 700;
    font-size: 92px;
    line-height: 1;
    letter-spacing: 1px;
    color: var(--ink);
  }
  .variant {
    position: absolute;
    left: 214px;
    top: 196px;
    font-family: "Roboto Slab", serif;
    font-weight: 700;
    font-size: 24px;
    letter-spacing: 1px;
    color: var(--band);
    z-index: 2;
  }
  .band {
    position: absolute;
    left: 0;
    right: 0;
    top: 222px;
    bottom: 0;
    background: var(--band);
  }
  .band__rule {
    position: absolute;
    left: 0;
    right: 0;
    top: 60px;
    border-top: 2px dashed rgba(255,255,255,0.75);
  }
  .band__rule--low { top: 140px; }
  .uses {
    position: absolute;
    left: 300px;
    top: 14px;
    display: flex;
    align-items: center;
    gap: 16px;
    font-family: "Lato", sans-serif;
    font-size: 20px;
    color: var(--cream);
  }
  .uses__icon {
    width: 38px;
    height: 32px;
    border-radius: 6px;
    background: rgba(255,255,255,0.28);
  }
  .uses__sep {
    width: 7px;
    height: 7px;
    border-radius: 50%;
    background: var(--cream);
  }
  .motto {
    position: absolute;
    left: 22px;
    top: 78px;
    font-family: "Oswald", sans-serif;
    font-weight: 500;
    font-size: 20px;
    line-height: 1.05;
    color: var(--cream);
  }
  .badge {
    position: absolute;
    left: 150px;
    top: 84px;
    padding: 3px 10px;
    border: 2px solid var(--cream);
    border-radius: 5px;
    text-align: center;
    font-family: "Oswald", sans-serif;
    color: var(--cream);
    line-height: 1.05;
  }
  .badge__small { font-size: 13px; letter-spacing: 0.5px; }
  .badge__big { font-size: 20px; font-weight: 700; }
  .claim {
    position: absolute;
    left: 410px;
    top: 78px;
    width: 120px;
    font-family: "Lato", sans-serif;
    font-size: 12px;
    line-height: 1.25;
    color: var(--cream);
  }
  .claim__leaf {
    position: absolute;
    left: 540px;
    top: 80px;
    width: 30px;
    height: 40px;
    border-radius: 6px;
    background: rgba(255,255,255,0.28);
  }
  .count {
    position: absolute;
    right: 90px;
    top: 76px;
    font-family: "Lato", sans-serif;
    font-size: 26px;
    color: var(--cream);
  }
  .count small { font-size: 16px; }
</style>
</head>
<body>
<main class="canvas">

  <section class="pack pack--original">
    <div class="pack__tab"></div>
    <div class="pack__label" role="img" aria-label="Light wood grain background">
      <div class="brand"><span class="brand__dot"></span>Marlo Bakery</div>
      <div class="product-line">-Tavira-</div>
      <div class="product-name">PIZZA BASES</div>
      <div class="variant">ORIGINAL</div>
      <div class="band">
        <div class="band__rule"></div>
        <div class="band__rule band__rule--low"></div>
        <div class="uses">
          <span class="uses__icon" role="img" aria-label="Toppings icon"></span><span>TOP it!</span><span class="uses__sep"></span>
          <span class="uses__icon" role="img" aria-label="Baking tray icon"></span><span>BAKE it!</span><span class="uses__sep"></span>
          <span class="uses__icon" role="img" aria-label="Folded bread icon"></span><span>FOLD it!</span><span class="uses__sep"></span>
          <span class="uses__icon" role="img" aria-label="Rolled wrap icon"></span><span>ROLL it!</span>
        </div>
        <div class="motto">USE IT AS<br>YOU LIKE!</div>
        <div class="badge"><div class="badge__small">PRESERVATIVE FREE</div><div class="badge__big">100% NATURAL</div></div>
        <div class="claim">Made handmade with 5 bases and natural olive oil.</div>
        <span class="claim__leaf" role="img" aria-label="Olive sprig"></span>
        <div class="count">5 <small>PCS.</small></div>
      </div>
    </div>
  </section>

  <section class="pack pack--garlic">
    <div class="pack__tab"></div>
    <div class="pack__label" role="img" aria-label="Light wood grain background">
      <div class="brand"><span class="brand__dot"></span>Marlo Bakery</div>
      <div class="product-line">-Tavira-</div>
      <div class="product-name">PIZZA BASES</div>
      <div class="variant">ROASTED GARLIC</div>
      <div class="band">
        <div class="band__rule"></div>
        <div class="band__rule band__rule--low"></div>
        <div class="uses">
          <span class="uses__icon" role="img" aria-label="Toppings icon"></span><span>TOP it!</span><span class="uses__sep"></span>
          <span class="uses__icon" role="img" aria-label="Baking tray icon"></span><span>BAKE it!</span><span class="uses__sep"></span>
          <span class="uses__icon" role="img" aria-label="Folded bread icon"></span><span>FOLD it!</span><span class="uses__sep"></span>
          <span class="uses__icon" role="img" aria-label="Rolled wrap icon"></span><span>ROLL it!</span>
        </div>
        <div class="motto">USE IT AS<br>YOU LIKE!</div>
        <div class="badge"><div class="badge__small">PRESERVATIVE FREE</div><div class="badge__big">100% NATURAL</div></div>
        <div class="claim">Made handmade with 5 bases and natural olive oil.</div>
        <span class="claim__leaf" role="img" aria-label="Olive sprig"></span>
        <div class="count">5 <small>PCS.</small></div>
      </div>
    </div>
  </section>

</main>
</body>
</html>
```